Pawpine Pantry

We need a word press template designed for our new Word press site.
We'd like to mimic the design of the old site somewhat:
http://www.pawpinepantry-example.com/
to be ported over to the new site:
http://www.pawpinepantry-example.com/wp
We like the ornamental dog bone style in the old sites's banner/navigation. We may want to mimic that somewhat in the new design.
We have a retail store in historic Portsmouth, NH and we bake gourmet dog teats and sell leashes, collars, outdoor gear, beds, soft-sided crates, interactive toys and premium dog & cat foods.

```html
<!DOCTYPE html>
<html lang="en">
<head>
<meta charset="utf-8">
<title>Pawpine Pantry</title>
<link href="https://fonts.googleapis.com/css2?family=Oswald:wght@500&family=Yanone+Kaffeesatz:wght@400;600&family=PT+Sans:wght@400;700&family=Arimo:wght@400;700&display=swap" rel="stylesheet">
<style>
:root{
  --forest:#013201;
  --forest-deep:#012401;
  --cream:#e6e0c1;
  --tile-top:#ffffff;
  --tile-bottom:#fbefcf;
  --gold:#f2d31b;
  --orange:#f7930b;
  --leaf:#7ba610;
  --ink:#3a3a3a;
  --white:#ffffff;
}
*{margin:0;padding:0;box-sizing:border-box}
html,body{width:1200px;height:764px;overflow:hidden;background:var(--forest)}
.page{position:relative;width:1200px;height:764px;background:var(--forest);font-family:"PT Sans",sans-serif}

.top-nav{position:absolute;left:0;top:0;width:1200px;height:35px;background:linear-gradient(90deg,var(--forest) 30%,#000 45%,#000 85%,var(--forest))}
.top-nav ul{list-style:none;position:absolute;left:445px;top:0;display:flex;height:35px;align-items:center}
.top-nav li{font-family:"Oswald",sans-serif;font-size:15px;color:var(--gold);text-transform:uppercase;padding:0 16px;border-left:1px solid #3f4a2a;line-height:16px;letter-spacing:-.2px}
.top-nav li:first-child{border-left:0}

.header{position:absolute;left:0;top:35px;width:1200px;height:112px;background:var(--cream);border-bottom:2px solid var(--forest-deep)}
.brand{position:absolute;left:160px;top:36px;display:flex;align-items:center;gap:8px}
.brand-dot{width:30px;height:30px;border-radius:50%;background:#d7262b}
.brand-name{font-family:"PT Sans",sans-serif;font-weight:700;font-size:18px;color:#7a3b12}
.partners{position:absolute;left:466px;top:0;display:flex;height:110px}
.partner{width:136px;height:110px;border-left:2px solid var(--forest-deep);background:linear-gradient(var(--tile-top) 20%,var(--tile-bottom));text-align:center;padding-top:30px;position:relative;color:var(--ink)}
.partner:last-child{border-right:2px solid var(--forest-deep)}
.partner b{display:block;font-size:16px;line-height:16px;font-weight:400;letter-spacing:-.3px}
.partner span{display:block;font-size:12px;margin-top:2px}
.partner i{position:absolute;right:8px;bottom:6px;width:8px;height:8px;border-right:1.5px solid #b59a50;border-bottom:1.5px solid #b59a50}
.social{position:absolute;left:1025px;top:10px;display:flex;flex-direction:column;gap:5px}
.social span{width:28px;height:28px;border-radius:4px;background:#3b3b3b}

.hero{position:absolute;left:99px;top:148px;width:990px;height:556px;overflow:hidden}
.hero-photo{position:absolute;inset:0;background:linear-gradient(180deg,#b9c6b4 0%,#5f8a3c 30%,#4c7a2a 55%,#6e9a3e 75%,#5d8a34 100%)}
.hero-copy{position:absolute;left:62px;top:70px;color:var(--white);font-family:"Yanone Kaffeesatz",sans-serif;text-shadow:2px 3px 4px rgba(0,0,0,.55)}
.hero-since{font-size:36px;line-height:34px;color:#f2f2f2}
.hero-title{font-size:66px;line-height:58px;font-weight:600;letter-spacing:-1px}
.hero-sub{font-size:28px;line-height:34px;margin-top:6px}
.learn-more{position:absolute;left:62px;top:249px;width:82px;height:17px;background:#111;color:var(--white);font-family:"Arimo",sans-serif;font-size:10px;line-height:17px;padding-left:6px}
.learn-more::after{content:"";position:absolute;right:6px;top:6px;border-left:4px solid #fff;border-top:3px solid transparent;border-bottom:3px solid transparent}

.news{position:absolute;left:61px;top:375px;width:255px;height:119px;background:rgba(40,50,25,.82);color:var(--white);font-family:"Arimo",sans-serif;font-size:10px}
.news-label{position:absolute;left:8px;top:102px;transform:rotate(-90deg);transform-origin:left top;font-family:"PT Sans",sans-serif;font-size:14px;color:#e3d28a;white-space:nowrap}
.news-item{position:absolute;left:41px;width:198px;line-height:12px;padding-bottom:5px;border-bottom:1px solid rgba(255,255,255,.3)}
.news-more{position:absolute;left:41px;top:96px;color:#f0d472;text-decoration:underline}

.badge{position:absolute;border-radius:50%}
.badge-gallery{left:655px;top:197px;width:260px;height:260px;border:5px solid var(--gold);background:linear-gradient(#8aa868,#5e8b32)}
.badge-products{left:508px;top:295px;width:180px;height:180px;border:5px solid var(--orange);background:#fbf5ea}
.badge-fun{left:665px;top:375px;width:144px;height:144px;border:5px solid var(--leaf);background:linear-gradient(#7f9c5a,#a76a2f)}
.badge-label{position:absolute;font-family:"PT Sans",sans-serif;font-weight:700;text-shadow:2px 2px 4px rgba(0,0,0,.45)}
.label-gallery{left:720px;top:150px;font-size:42px;color:var(--gold);letter-spacing:-1px}
.label-products{left:397px;top:345px;font-size:38px;line-height:36px;color:var(--orange);letter-spacing:-1px}
.label-fun{left:788px;top:440px;font-size:42px;color:var(--leaf)}

.slide-arrow{position:absolute;top:397px}
.arrow-prev{left:41px}
.arrow-next{left:1097px}

.footer-links{position:absolute;left:163px;top:728px;display:flex;font-family:"Arimo",sans-serif;font-weight:700;font-size:11px;color:var(--white)}
.footer-links span+span::before{content:"";display:inline-block;width:3px;height:3px;background:var(--white);margin:0 8px 2px}
.copyright{position:absolute;left:743px;top:728px;font-family:"Arimo",sans-serif;font-size:10px;color:var(--white)}
</style>
</head>
<body>
<div class="page">
  <nav class="top-nav">
    <ul><li>Home</li><li>About Us</li><li>Our Products</li><li>Our Store</li><li>Links</li><li>News</li><li>Contact Us</li></ul>
  </nav>

  <header class="header">
    <div class="brand"><span class="brand-dot"></span><span class="brand-name">Pawpine Pantry</span></div>
    <div class="partners">
      <div class="partner"><b>Golden Meadow<br>Health</b><span>Products</span><i></i></div>
      <div class="partner"><b>Harlow Animal<br>Foundation</b><span>U.S</span><i></i></div>
      <div class="partner"><b>Gentle<br>Paw</b><span>Pet Services</span><i></i></div>
      <div class="partner"><b>Riverbend<br>Obedience</b><span>Club</span><i></i></div>
    </div>
    <div class="social" aria-label="Social links"><span></span><span></span><span></span></div>
  </header>

  <section class="hero">
    <div class="hero-photo" role="img" aria-label="Two shepherd dogs sitting on a green lawn in front of trees"></div>
    <div class="hero-copy">
      <div class="hero-since">Since 2001,</div>
      <div class="hero-title">Pawpine Pantry</div>
      <div class="hero-sub">has been providing the Seacoast</div>
    </div>
    <div class="learn-more">Learn More</div>

    <div class="news">
      <div class="news-label">News &amp; Offers</div>
      <div class="news-item" style="top:14px">Sprng 2013<br>We've moved up the road a few blocks to<br>140 Harbor Street</div>
      <div class="news-item" style="top:62px">Fall 2010<br>Well it has been a tough winter for us...</div>
      <div class="news-more">More News &amp; Offers</div>
    </div>

    <div class="badge badge-gallery" role="img" aria-label="Puppy sitting in a meadow"></div>
    <div class="badge badge-products" role="img" aria-label="Baked dog bone treats"></div>
    <div class="badge badge-fun" role="img" aria-label="Person playing with a group of dogs"></div>
    <div class="badge-label label-gallery">Gallery</div>
    <div class="badge-label label-products">Our<br>Products</div>
    <div class="badge-label label-fun">fun</div>
  </section>

  <svg class="slide-arrow arrow-prev" width="50" height="56" viewBox="0 0 50 56" aria-label="Previous slide">
    <ellipse cx="25" cy="28" rx="22" ry="25" fill="#3c5a3c" stroke="#e8e8e8" stroke-width="3"/>
    <path d="M32 14 L14 28 L32 42 Z" fill="#e8e8e8"/>
  </svg>
  <svg class="slide-arrow arrow-next" width="50" height="56" viewBox="0 0 50 56" aria-label="Next slide">
    <ellipse cx="25" cy="28" rx="22" ry="25" fill="#3c5a3c" stroke="#e8e8e8" stroke-width="3"/>
    <path d="M18 14 L36 28 L18 42 Z" fill="#e8e8e8"/>
  </svg>

  <footer>
    <div class="footer-links"><span>Press</span><span>Careers</span><span>Contact Us</span><span>Terms &amp; Conditions</span><span>Sitemap</span></div>
    <div class="copyright">© Copyright 2013, all rights reserved with <b>pawpine pantry</b></div>
  </footer>
</div>
</body>
</html>
```